Horse Brush Package design -

I need a design for a box - required for a rubber horse brush used for grooming and removing excess hair. The Brand is 'Maple Ridge Equestrian' and we develop top quality horse products. The design should be classy and professional

Box size is 21.5cm Length * 2cm high * 5 cm wide
Photo of logo and brush attached.
Box needs to have logo and description on front
Barcode on back.
Additional designs and photos can be added as you see fit.

"Horse Deshedding & Grooming Brush"
Brush away excess coat and dander
Gently remove dirt and mud
Soft, flexible design to gently groom around legs, ears and face.
Used when washing gives a deep clean to remove dirt
Gentle massage for increasing circulation
Durable, gentle, and kind to the horse

Target Market(s)

Horse Owners

Requirements
Must have
• Logo on the front, space for barcode on the back
Nice to have
• A nice horse photo would be suitable

```html
<!DOCTYPE html>
<html lang="en">
<head>
<meta charset="utf-8">
<title>Maple Ridge Equestrian – Horse Deshedding &amp; Grooming Brush</title>
<link href="https://fonts.googleapis.com/css2?family=Montserrat:wght@300;400;600;700;800&display=swap" rel="stylesheet">
<style>
  :root {
    --bg-deep: #22262e;
    --bg-mid: #2b3039;
    --bg-light: #343a45;
    --gold: #e2c48f;
    --gold-soft: #cfae75;
    --white: #ffffff;
    --grey: #9a9ea6;
    --stripe: rgba(120, 130, 150, 0.35);
  }
  * { margin: 0; padding: 0; box-sizing: border-box; }
  html, body { width: 1200px; height: 5156px; overflow: hidden; }
  body { font-family: "Montserrat", sans-serif; background: var(--bg-deep); }

  .box-panel {
    position: relative;
    width: 1200px;
    height: 5156px;
    overflow: hidden;
    background: linear-gradient(180deg, var(--bg-mid) 0%, var(--bg-deep) 45%, var(--bg-mid) 100%);
  }
  .top-sheen {
    position: absolute; inset: 0 0 auto 0; height: 2200px;
    background: linear-gradient(225deg, var(--bg-light) 0%, var(--bg-light) 28%, transparent 28.2%);
    opacity: 0.7;
  }

  .brand-mark {
    position: absolute;
    left: 640px; top: 1240px;
    transform: translate(-50%, -50%) rotate(-90deg);
    color: var(--gold);
    font-weight: 400;
    font-size: 128px;
    line-height: 1.05;
    letter-spacing: 6px;
    text-align: left;
    white-space: nowrap;
  }

  .dot-field {
    position: absolute; left: 0; top: 2230px; width: 1200px; height: 2926px;
    background: linear-gradient(180deg, rgba(255,255,255,0.06), rgba(255,255,255,0.03));
  }

  .product-title {
    position: absolute; left: 0; top: 2350px; width: 1200px;
    text-align: center; line-height: 1;
  }
  .title-gold {
    display: block; color: var(--gold); font-weight: 300;
    font-size: 240px; letter-spacing: 4px;
  }
  .title-bold {
    display: block; color: var(--white); font-weight: 800;
    font-size: 166px; letter-spacing: -2px; margin-top: 28px; white-space: nowrap;
  }
  .title-bold .amp { color: var(--grey); }
  .title-gold.last { margin-top: 30px; }

  .stripes { position: absolute; left: 0; top: 3200px; }

  .feature {
    position: absolute;
    transform-origin: 0 0;
    transform: rotate(-45deg);
    color: var(--white);
    white-space: nowrap;
  }
  .feature-main { display: block; font-weight: 600; font-size: 46px; line-height: 1.1; }
  .feature-sub { display: block; font-weight: 400; font-size: 32px; line-height: 1; text-align: right; }
</style>
</head>
<body>
<main class="box-panel">
  <div class="top-sheen"></div>

  <div class="brand-mark">MAPLE RIDGE<br>EQUESTRIAN</div>

  <div class="dot-field" role="img" aria-label="Decorative white dot pattern background"></div>

  <h1 class="product-title">
    <span class="title-gold">HORSE</span>
    <span class="title-bold">DESHEDDING</span>
    <span class="title-bold"><span class="amp">&amp;</span> GROOMING</span>
    <span class="title-gold last">BRUSH</span>
  </h1>

  <svg class="stripes" width="1200" height="1956" viewBox="0 0 1200 1956" aria-hidden="true">
    <g stroke="var(--stripe)" stroke-width="14" stroke-linecap="round">
      <line x1="1000" y1="160" x2="600" y2="560"/>
      <line x1="1060" y1="400" x2="700" y2="760"/>
      <line x1="1080" y1="680" x2="760" y2="1000"/>
    </g>
  </svg>

  <ul class="features" style="list-style:none">
    <li class="feature" style="left:118px; top:4020px"><span class="feature-main">Brush away excess coat and dander</span></li>
    <li class="feature" style="left:136px; top:4295px"><span class="feature-main">Gently remove dirt and mud</span></li>
    <li class="feature" style="left:142px; top:4585px"><span class="feature-main">Soft, flexible design to gently groom</span><span class="feature-sub">around legs, ears and face.</span></li>
    <li class="feature" style="left:142px; top:4874px"><span class="feature-main">Used when washing gives a deep</span><span class="feature-sub">clean to remove dirt</span></li>
    <li class="feature" style="left:188px; top:5087px"><span class="feature-main">Gentle massage for increasing circulation</span></li>
    <li class="feature" style="left:493px; top:5087px"><span class="feature-main">Durable, gentle, and kind to</span><span class="feature-sub">the horse</span></li>
  </ul>
</main>
</body>
</html>
```